Stationary and business cards for TerraQuestia-an Education, Enrichment, and Conservation Ctr
TerraQuestia (top line) Education, Enrichment, Conservation
Stationary and business cards for TerraQuestia-an Education, Enrichment, and Conservation Ctr - Animals
Creative Brief
Bright & Fun-filled
Tova Ruth Kellerby-Doane
Executive Director
483 Brindwick Rd. suite 300 Ostervale, MD 20947
tovark@mailcove.example
www.TerraQuestia.example
I would like it to have foliage or vines coming out of the sides like rainforest...maybe a red eye tree frog somewhere and a morpho butterfly... Want it to be simple but classy....and want to be able to have the names and contact info to be interchangeable for all my employees. For the stationary I want the logo somewhere as well. Thank you!
The logo
tovark tovark
I like the leaf addition, but instead of putting it in the back...can you replace the lines in the front of the business card and putting the leaf outlines? That goes better with our theme than "professional" looking lines etc.... thanks!
I can't find how to attach the logo?
quintonhalvard7314065 quintonhalvard7314065
i need the logo logo are not attach in Brief
you can go to our website to get an idea of who we are www.TerraQuestia.example and see our logo.

```html
<!DOCTYPE html>
<html lang="en">
<head>
<meta charset="utf-8">
<title>TerraQuestia Business Card</title>
<link href="https://fonts.googleapis.com/css2?family=Open+Sans:wght@400;600;700&display=swap" rel="stylesheet">
<style>
  :root {
    --backdrop: #d9d7d4;
    --earth: #5e3b1c;
    --leaf: #3a9a1f;
    --paper: #ffffff;
    --ink-light: #f4efe8;
  }
  * { margin: 0; padding: 0; box-sizing: border-box; }
  html, body { width: 1200px; height: 803px; overflow: hidden; }
  body {
    background: var(--backdrop);
    font-family: "Open Sans", Arial, sans-serif;
    position: relative;
  }
  .card {
    position: absolute;
    width: 540px;
    height: 309px;
    top: 247px;
    overflow: hidden;
    background: var(--earth);
    box-shadow: 0 6px 18px rgba(0,0,0,0.18);
  }
  .card--front { left: 45px; }
  .card--back { left: 615px; }
  .card__shapes { position: absolute; inset: 0; width: 100%; height: 100%; }

  .brand {
    position: absolute;
    left: 40px; top: 70px;
    display: flex; align-items: center; gap: 10px;
  }
  .brand__dot {
    width: 16px; height: 16px; border-radius: 50%;
    background: var(--leaf);
  }
  .brand__name {
    font-weight: 700; font-size: 36px; line-height: 1; color: var(--earth);
    letter-spacing: 0.5px;
  }

  .contact {
    position: absolute; color: var(--ink-light);
    font-size: 11px; line-height: 1.45;
    display: flex; align-items: flex-start; gap: 10px;
  }
  .contact svg { flex: none; margin-top: 2px; }
  .contact--phone { left: 26px; top: 180px; }
  .contact--address { left: 26px; top: 222px; }
  .contact--email { left: 190px; top: 270px; font-size: 12px; align-items: center; }

  .web-link {
    position: absolute; right: 24px; top: 181px;
    color: var(--paper);
    font-size: 12px; font-weight: 600; line-height: 1;
  }

  .holder {
    position: absolute; right: 28px; top: 26px;
    text-align: right; color: var(--paper);
  }
  .holder__name { font-size: 15px; font-weight: 700; letter-spacing: 1px; text-transform: uppercase; }
  .holder__title { font-size: 11px; margin-top: 2px; }
</style>
</head>
<body>

  <section class="card card--front">
    <svg class="card__shapes" viewBox="0 0 540 309" preserveAspectRatio="none" aria-hidden="true">
      <rect x="0" y="36" width="540" height="118" fill="var(--leaf)"/>
      <rect x="0" y="42" width="470" height="104" fill="var(--paper)"/>
      <path d="M0 154 H540 V214 H340 C300 214 290 164 250 164 H0 Z" fill="var(--leaf)"/>
    </svg>

    <div class="brand">
      <span class="brand__dot"></span>
      <span class="brand__name">TerraQuestia</span>
    </div>

    <div class="contact contact--phone">
      <svg width="14" height="14" viewBox="0 0 24 24" aria-hidden="true">
        <path fill="var(--ink-light)" d="M6.6 10.8a15.1 15.1 0 0 0 6.6 6.6l2.2-2.2c.3-.3.7-.4 1-.2 1.1.4 2.3.6 3.6.6.6 0 1 .4 1 1V20c0 .6-.4 1-1 1C10.6 21 3 13.4 3 4c0-.6.4-1 1-1h3.5c.6 0 1 .4 1 1 0 1.3.2 2.5.6 3.6.1.3 0 .7-.2 1z"/>
      </svg>
      <p>012 555 0147<br>012 555 0148</p>
    </div>

    <div class="contact contact--address">
      <svg width="14" height="14" viewBox="0 0 24 24" aria-hidden="true">
        <path fill="var(--ink-light)" d="M12 3 2 12h3v8h5v-5h4v5h5v-8h3z"/>
      </svg>
      <p>483 Brindwick Rd. suite 300<br>Ostervale, MD 20947</p>
    </div>

    <p class="web-link">www.TerraQuestia.example</p>

    <div class="contact contact--email">
      <svg width="20" height="14" viewBox="0 0 20 14" aria-hidden="true">
        <rect x="0.75" y="0.75" width="18.5" height="12.5" fill="none" stroke="var(--ink-light)" stroke-width="1.5"/>
        <path d="M1 1 10 8 19 1" fill="none" stroke="var(--ink-light)" stroke-width="1.5"/>
      </svg>
      <p>tovark@mailcove.example</p>
    </div>
  </section>

  <section class="card card--back">
    <svg class="card__shapes" viewBox="0 0 540 309" preserveAspectRatio="none" aria-hidden="true">
      <path d="M0 30 C90 40 150 110 250 110 C330 110 420 70 540 70 V309 H0 Z" fill="var(--leaf)"/>
      <path d="M120 150 C150 120 220 128 290 130 C360 132 430 110 540 105 V260 C430 250 380 240 330 220 C260 195 170 200 120 150 Z" fill="var(--paper)"/>
      <path d="M0 260 C150 250 330 250 540 290 V309 H0 Z" fill="var(--earth)"/>
    </svg>
    <div class="holder">
      <p class="holder__name">Tova Ruth Kellerby-Doane</p>
      <p class="holder__title">Executive Director</p>
    </div>
  </section>

</body>
</html>
```